Dance School poster for end of year dance concert for mainly young girls.

We need an A3 portrait poster for our end of year concert.
Designs are attached of posters from previous 2 years as a reference only.
The theme of our concert this year is "Let's Dance" which we want to convey a general feel of energy & fun with dance.
Dance styles in the concert include Jazz & Hip Hop.
Bright colors are preferred in the design.

Target Market(s)

The concert is attended by several hundred family & friends

Industry/Entity Type

Dance Studio

Requirements
Must have
• Must have
• Let's Dance
• BRK logo (file supplied)
• 'The Maribel Crowe Dancers' (font is Mistral)
• Date of the concert: Saturday 14th November 2015
• Pellow Theatre, Saint Fenwick College Dalebrook
Nice to have
• We like clean design with no cluttered imagery.

```html
<!DOCTYPE html>
<html lang="en">
<head>
<meta charset="utf-8">
<title>Let's Dance – The Maribel Crowe Dancers</title>
<link rel="stylesheet" href="https://fonts.googleapis.com/css2?family=Bebas+Neue&family=Kaushan+Script&family=Oswald:wght@500;700&display=swap">
<style>
  :root {
    --frame: #ffffff;
    --magenta: #e0127e;
    --violet: #5a1a9a;
    --blue: #1a7fe0;
    --deep: #2a0a4a;
    --ribbon: #d8141c;
    --ribbon-dark: #8e0a0f;
    --gold-light: #fff2b0;
    --gold: #f2c230;
    --gold-dark: #a8700e;
    --ink-light: #ffffff;
  }
  html, body {
    margin: 0;
    padding: 0;
    width: 849px;
    height: 1200px;
    overflow: hidden;
    background: var(--frame);
  }
  .poster {
    position: relative;
    width: 849px;
    height: 1200px;
    background: var(--frame);
    overflow: hidden;
  }
  .backdrop {
    position: absolute;
    inset: 14px;
    background:
      radial-gradient(ellipse 45% 35% at 50% 48%, rgba(255, 190, 230, 0.55), transparent 70%),
      radial-gradient(ellipse 60% 60% at 50% 30%, rgba(120, 40, 180, 0.5), transparent 75%),
      linear-gradient(90deg, var(--magenta) 0%, #c01490 25%, var(--violet) 50%, #2a4fc8 75%, var(--blue) 100%);
  }
  .backdrop::after {
    content: "";
    position: absolute;
    inset: 0;
    background: linear-gradient(180deg, rgba(20, 0, 40, 0.35) 0%, transparent 25%, transparent 70%, rgba(20, 0, 40, 0.45) 100%);
  }
  .brand-mark {
    position: absolute;
    top: 28px;
    left: 50%;
    transform: translateX(-50%);
    display: flex;
    align-items: center;
    gap: 10px;
    z-index: 3;
  }
  .brand-mark .dot {
    width: 22px;
    height: 22px;
    border-radius: 50%;
    background: var(--ink-light);
  }
  .brand-mark .name {
    font-family: "Oswald", sans-serif;
    font-weight: 700;
    font-size: 46px;
    line-height: 1;
    color: var(--ink-light);
    letter-spacing: 2px;
  }
  .ribbon {
    position: absolute;
    top: 80px;
    left: 70px;
    width: 709px;
    height: 150px;
    z-index: 2;
  }
  .school-name {
    position: absolute;
    top: 118px;
    left: 0;
    width: 849px;
    text-align: center;
    font-family: "Kaushan Script", cursive;
    font-size: 52px;
    line-height: 1;
    color: var(--gold-light);
    z-index: 3;
  }
  .presents {
    position: absolute;
    top: 240px;
    left: 0;
    width: 849px;
    text-align: center;
    font-family: "Oswald", sans-serif;
    font-weight: 500;
    font-size: 34px;
    letter-spacing: 3px;
    color: var(--ink-light);
  }
  .headline {
    position: absolute;
    top: 350px;
    left: 0;
    width: 849px;
    margin: 0;
    text-align: center;
    font-family: "Bebas Neue", sans-serif;
    font-weight: 400;
    font-size: 178px;
    line-height: 0.86;
    letter-spacing: 4px;
    background: linear-gradient(180deg, var(--gold-light) 0%, var(--gold) 45%, var(--gold-dark) 55%, var(--gold) 80%, var(--gold-light) 100%);
    -webkit-background-clip: text;
    background-clip: text;
    color: transparent;
    -webkit-text-stroke: 3px #7a4a08;
    filter: drop-shadow(0 6px 10px rgba(30, 0, 40, 0.6));
  }
  .headline span { display: block; }
  .headline .line-two { font-size: 206px; }
  .stars {
    position: absolute;
    top: 700px;
    left: 134px;
    width: 580px;
    height: 130px;
    filter: drop-shadow(0 4px 8px rgba(30, 0, 40, 0.5));
  }
  .event-details {
    position: absolute;
    top: 870px;
    left: 0;
    width: 849px;
    text-align: center;
    font-family: "Bebas Neue", sans-serif;
    font-size: 56px;
    line-height: 0.9;
    letter-spacing: 1px;
    color: var(--ink-light);
    text-shadow: 0 3px 6px rgba(20, 0, 40, 0.5);
  }
  .event-details p { margin: 0; }
  .event-details strong {
    font-family: "Oswald", sans-serif;
    font-weight: 700;
    font-size: 50px;
  }
</style>
</head>
<body>
  <main class="poster">
    <div class="backdrop" role="img" aria-label="Bright stage backdrop of glowing magenta, violet and blue light dots"></div>

    <div class="brand-mark">
      <span class="dot"></span>
      <span class="name">BRK</span>
    </div>

    <svg class="ribbon" viewBox="0 0 709 150" aria-hidden="true">
      <defs>
        <linearGradient id="ribbonFace" x1="0" y1="0" x2="0" y2="1">
          <stop offset="0" stop-color="#f0343a"/>
          <stop offset="1" stop-color="#b80e14"/>
        </linearGradient>
      </defs>
      <polygon points="0,40 70,40 70,130 0,130 28,85" fill="var(--ribbon-dark)"/>
      <polygon points="709,40 639,40 639,130 709,130 681,85" fill="var(--ribbon-dark)"/>
      <polygon points="50,110 70,130 70,110" fill="#5e0609"/>
      <polygon points="659,110 639,130 639,110" fill="#5e0609"/>
      <path d="M50 18 Q354 -4 659 18 L659 110 Q354 88 50 110 Z" fill="url(#ribbonFace)"/>
    </svg>
    <div class="school-name">The Maribel Crowe Dancers</div>

    <div class="presents">PRESENTS</div>

    <h1 class="headline">
      <span class="line-one">LET'S</span>
      <span class="line-two">DANCE</span>
    </h1>

    <svg class="stars" viewBox="0 0 580 130" aria-hidden="true">
      <defs>
        <linearGradient id="starGold" x1="0" y1="0" x2="0" y2="1">
          <stop offset="0" stop-color="#fff2b0"/>
          <stop offset="0.5" stop-color="#f2c230"/>
          <stop offset="1" stop-color="#a8700e"/>
        </linearGradient>
        <polygon id="star" points="0,-50 11.8,-16.2 47.6,-15.5 19,6.2 29.4,40.5 0,20 -29.4,40.5 -19,6.2 -47.6,-15.5 -11.8,-16.2"/>
      </defs>
      <use href="#star" transform="translate(62 72) scale(0.95)" fill="url(#starGold)" stroke="#7a4a08" stroke-width="2"/>
      <use href="#star" transform="translate(176 66) scale(1.08)" fill="url(#starGold)" stroke="#7a4a08" stroke-width="2"/>
      <use href="#star" transform="translate(290 62) scale(1.2)" fill="url(#starGold)" stroke="#7a4a08" stroke-width="2"/>
      <use href="#star" transform="translate(404 66) scale(1.08)" fill="url(#starGold)" stroke="#7a4a08" stroke-width="2"/>
      <use href="#star" transform="translate(518 72) scale(0.95)" fill="url(#starGold)" stroke="#7a4a08" stroke-width="2"/>
    </svg>

    <section class="event-details">
      <p>SATURDAY <strong>14TH</strong></p>
      <p>OF <strong>NOVEMBER</strong> 2015</p>
      <p>@ <strong>PELLOW THEATRE,</strong></p>
      <p>SAINT FENWICK COLLEGE</p>
      <p>DALEBROOK</p>
    </section>
  </main>
</body>
</html>
```